Vantoralis 'Private Prism' Book Cover Design project

I need to revise the book cover design I have for my coming book. The design I created through CraftHerd is great but the book has grown and changed so I'm looking for an alternative/option design. I can then choose later from the different options.

I need a book cover that represents the unique book I am creating.

Book Title:
Your True Spectrum

Subtitle: Walking Your Path and Not Your Tag

The book is targeting all readers with a special focus on same sex attracted readers. It should not have stereotypical images.

I am including a file of the book cover I have had designed. The back cover blurb, author info and author pic will remain the same. The colouring of the back cover and spine will, of course, change to match the colouring of the front cover.

The new title will be on the spine and the new title wording.

The front cover will be markedly different using the bold images and rainbow colours of the images found in the files I am uploading for you.

I am thinking of a large boldly coloured rainbow face with the title and subtitle ON the image. The image will be the whole cover. It will fill the cover as much as possible with the text added onto the pic.

The bold pictures I am including will give you the idea of what I'm looking for.

ANY of the images I've uploaded can be used as the actual front cover image OR the designer might have/find some suitable image to be used. The image is to be large and bold and fill the cover. Hopefully a positive energy.
It needs to be eye-catching and striking and bold and positive.

So...the book cover sample file I've provided can keep the back cover with completely new colouring. The front cover is completely new with new image, wording and energy.

It is to be a rainbow coloured face or figure for the cover image.

I hope that is clear enough for you. I'm very happy to discuss and clarify these ideas with the designer. Looking forward to another great CraftHerd experience.

Target Market(s)

Wide audience with special focus on Same Sex Attracted individuals

Font styles to use
Script
Other font styles liked:
• Some form of handwriting font to make the book title and text appear more personal....as if handwritten by me.

Requirements
Must have
• Boldness, Quirky, Rainbow Colour, Image to fill the cover, maybe dark cover contrasting background.
Nice to have
• A well balanced back cover especially in the area where the barcode will be placed.
Should not have
• No stereotypical images

```html
<!DOCTYPE html>
<html lang="en">
<head>
<meta charset="utf-8">
<title>Your True Spectrum – Book Cover</title>
<link rel="stylesheet" href="https://fonts.googleapis.com/css2?family=Patrick+Hand&family=PT+Sans&display=swap">
<style>
  :root {
    --page: #ffffff;
    --ink: #3d3c3d;
    --band-edge: #8c8a8b;
    --band-mid: #ffffff;
    --teal-grey: #74908e;
    --orange: #f25a1c;
    --pink: #f59ccb;
    --red: #d8121f;
    --yellow: #fbe640;
    --blue: #2f7fd6;
    --maroon: #5e0f16;
    --violet: #9a6ad8;
    --cream: #fff4d8;
    --aqua: #4fb8c8;
  }
  html, body {
    margin: 0;
    padding: 0;
    width: 1200px;
    height: 960px;
    overflow: hidden;
    background: var(--page);
  }
  .canvas {
    position: relative;
    width: 1200px;
    height: 960px;
    background: var(--page);
  }
  .cover {
    position: absolute;
    left: 255px;
    top: 97px;
    width: 690px;
    height: 765px;
  }
  .portrait-art {
    position: absolute;
    left: 0;
    top: 0;
    width: 690px;
    height: 583px;
    background:
      radial-gradient(ellipse 14% 12% at 56% 52%, var(--cream) 0%, var(--cream) 45%, rgba(255,244,216,0) 100%),
      radial-gradient(ellipse 18% 10% at 54% 76%, var(--red) 0%, var(--red) 55%, rgba(216,18,31,0) 100%),
      radial-gradient(ellipse 26% 16% at 48% 8%, var(--yellow) 0%, var(--yellow) 50%, rgba(251,230,64,0) 100%),
      radial-gradient(ellipse 22% 14% at 34% 18%, var(--pink) 0%, var(--pink) 50%, rgba(245,156,203,0) 100%),
      radial-gradient(ellipse 16% 30% at 92% 40%, var(--orange) 0%, var(--orange) 55%, rgba(242,90,28,0) 100%),
      radial-gradient(ellipse 14% 20% at 40% 60%, var(--aqua) 0%, var(--aqua) 45%, rgba(79,184,200,0) 100%),
      radial-gradient(ellipse 18% 22% at 30% 44%, var(--violet) 0%, var(--violet) 50%, rgba(154,106,216,0) 100%),
      radial-gradient(ellipse 34% 22% at 62% 96%, var(--maroon) 0%, var(--maroon) 40%, rgba(94,15,22,0) 100%),
      radial-gradient(ellipse 18% 24% at 6% 50%, var(--orange) 0%, var(--orange) 55%, rgba(242,90,28,0) 100%),
      radial-gradient(ellipse 14% 18% at 14% 78%, var(--pink) 0%, var(--pink) 50%, rgba(245,156,203,0) 100%),
      radial-gradient(ellipse 10% 20% at 99% 82%, var(--blue) 0%, var(--blue) 50%, rgba(47,127,214,0) 100%),
      radial-gradient(ellipse 20% 20% at 72% 62%, var(--red) 0%, var(--red) 45%, rgba(216,18,31,0) 100%),
      linear-gradient(100deg, var(--teal-grey) 0%, var(--teal-grey) 20%, #c98a6a 40%, var(--orange) 70%, var(--red) 88%, var(--teal-grey) 100%);
  }
  .portrait-art.lower {
    top: 737px;
    height: 28px;
    background: linear-gradient(90deg, #5aa0e0 0%, var(--violet) 28%, var(--blue) 52%, var(--pink) 78%, var(--orange) 100%);
  }
  .author-tag {
    position: absolute;
    left: 503px;
    top: 11px;
    width: 187px;
    height: 48px;
    background: linear-gradient(180deg, #ffffff 0%, #ffffff 60%, #d9d8d8 100%);
    clip-path: polygon(0 20%, 8% 14%, 15% 22%, 24% 10%, 33% 18%, 42% 8%, 52% 16%, 61% 6%, 70% 14%, 80% 4%, 90% 12%, 100% 2%, 100% 92%, 88% 96%, 76% 90%, 62% 98%, 50% 90%, 38% 97%, 26% 89%, 14% 96%, 6% 84%, 0 90%);
    display: flex;
    align-items: center;
    justify-content: flex-end;
    padding-right: 30px;
    box-sizing: border-box;
  }
  .author-name {
    font-family: "PT Sans", Arial, sans-serif;
    font-size: 19px;
    color: var(--ink);
    padding-top: 4px;
  }
  .title-band {
    position: absolute;
    left: 0;
    top: 596px;
    width: 690px;
    height: 134px;
    background: linear-gradient(180deg, var(--band-edge) 0%, #d8d7d7 12%, var(--band-mid) 28%, var(--band-mid) 72%, #d0cfcf 88%, var(--band-edge) 100%);
    clip-path: polygon(0 5%, 5% 3%, 11% 6%, 18% 2%, 26% 5%, 34% 1%, 43% 4%, 51% 2%, 60% 5%, 68% 1%, 77% 4%, 85% 2%, 93% 5%, 100% 3%, 100% 96%, 92% 98%, 83% 95%, 74% 99%, 65% 96%, 55% 99%, 46% 95%, 36% 98%, 27% 96%, 17% 99%, 8% 95%, 0 98%);
    text-align: center;
  }
  .book-title {
    margin: 27px 0 0;
    font-family: "Patrick Hand", cursive;
    font-weight: 400;
    font-size: 46px;
    line-height: 1;
    letter-spacing: 4px;
    color: var(--ink);
    -webkit-text-stroke: 1.6px var(--ink);
  }
  .book-subtitle {
    margin: 10px 0 0;
    font-family: "Patrick Hand", cursive;
    font-size: 24px;
    line-height: 1;
    letter-spacing: 1.8px;
    color: var(--ink);
  }
</style>
</head>
<body>
  <div class="canvas">
    <div class="cover">
      <div class="portrait-art" role="img" aria-label="Bold palette-knife portrait painted in vivid rainbow colours filling the cover"></div>
      <div class="author-tag"><span class="author-name">COLM ARDAGH</span></div>
      <div class="title-band">
        <h1 class="book-title">YOUR TRUE SPECTRUM</h1>
        <p class="book-subtitle">Walking Your Path and Not Your Tag</p>
      </div>
      <div class="portrait-art lower" role="img" aria-label="Lower edge of the rainbow portrait painting"></div>
    </div>
  </div>
</body>
</html>
```